QRV-TB 2018 Recycling Rate Report

We need a design for our 2018 Recycling Rate Report on Expanded Polystyrene. We want to move from a larger booklet style to a two page document. The report from last year - which was done as a booklet - is attached to provide an example of our style and design.The primary items that must be included (but not limited to) the information on pages 3, 5 & 7. The graphs must include room for 2018 data.To view our typical company design/style please see our website at www.qrvtradeboard.org. Our primary RGB colors are: (187,140,9); (94,47,29); (94,138,164); and (164,167,15). Secondary RGB colors are (249,162,28) and (218,210,208). Our title/header font is DIN Next LT Pro and our copy font is Calibri 10.5 pt. We can deviate from the font specification if beneficial and welcome interesting text treatments and typography.

Target Market(s)

Recycling facilities & general public.

Font styles to use
Sans Serif

Requirements
Must have
• Information presentation must be clean and easy to reference.

```html
<!DOCTYPE html>
<html lang="en">
<head>
<meta charset="utf-8">
<title>EPS Recycling Data</title>
<link href="https://fonts.googleapis.com/css2?family=Montserrat:wght@300;400;700&family=Carlito&display=swap" rel="stylesheet">
<style>
  :root {
    --gold: #b98d2f;
    --brown: #5c2e1f;
    --blue: #5e8aa4;
    --green: #a4a83b;
    --green-text: #9a9e34;
    --orange: #f9a21f;
    --stone: #dad3d0;
    --ink: #1f1a18;
    --muted: #8b807b;
    --pale: #dcd5d3;
    --white: #ffffff;
  }
  * { margin: 0; padding: 0; box-sizing: border-box; }
  html, body { width: 928px; height: 1200px; overflow: hidden; }
  body { background: var(--stone); font-family: "Carlito", "Calibri", sans-serif; color: var(--ink); }
  .page { position: relative; width: 928px; height: 1200px; overflow: hidden; background: var(--stone); }

  .header-band { position: absolute; left: 0; top: 0; width: 928px; height: 274px; background: var(--gold); }
  .section-title {
    position: absolute; left: 74px; top: 86px;
    font-family: "Montserrat", sans-serif; font-weight: 300;
    font-size: 92px; line-height: 1; color: var(--white); letter-spacing: 1px;
  }
  .intro {
    position: absolute; left: 396px; top: 74px; width: 470px;
    font-size: 14px; line-height: 19.6px; color: var(--white);
  }

  .total-band { position: absolute; left: 0; top: 274px; width: 928px; height: 237px; background: var(--brown); }
  .total-block { position: absolute; left: 40px; top: 36px; width: 316px; text-align: center; font-family: "Montserrat", sans-serif; }
  .total-year { font-size: 32px; font-weight: 400; color: var(--muted); line-height: 1.1; }
  .total-unit { font-size: 16px; font-weight: 400; color: var(--muted); line-height: 1.2; }
  .total-value { font-size: 112px; font-weight: 700; color: var(--pale); line-height: 1; margin-top: 4px; letter-spacing: -1px; }
  .total-photo {
    position: absolute; left: 422px; top: 0; width: 440px; height: 237px;
    background: radial-gradient(ellipse at 55% 45%, #f2f2f2 0%, #dcdcdc 55%, #c4c4c4 100%);
  }

  .chart-title {
    position: absolute; left: 0; top: 546px; width: 928px; text-align: center;
    font-family: "Montserrat", sans-serif; font-weight: 400; font-size: 27px; color: var(--ink);
  }
  .chart-subtitle {
    position: absolute; left: 0; top: 585px; width: 928px; text-align: center;
    font-family: "Montserrat", sans-serif; font-weight: 400; font-size: 17px; color: var(--ink);
  }
  .chart { position: absolute; left: 0; top: 600px; width: 928px; height: 400px; }
  .chart text { font-family: "Montserrat", sans-serif; }

  .summary {
    position: absolute; left: 60px; top: 1022px; width: 808px; text-align: center;
    font-size: 15.6px; line-height: 19.9px; color: var(--ink);
  }

  .footer-blue { position: absolute; left: 0; top: 1151px; width: 765px; height: 49px; background: var(--blue); }
  .footer-gold { position: absolute; left: 765px; top: 1151px; width: 163px; height: 49px; background: var(--gold); }
</style>
</head>
<body>
<main class="page">
  <section class="header-band">
    <h1 class="section-title">DATA</h1>
    <p class="intro">More than 65 million pounds of EPS were recycled during calendar year 2017. This figure includes 25.9 million pounds of post-consumer packaging and 39.0 million pounds of post-industrial recovery. Post-consumer is defined as any material that is recycled after its intended end-use while post-industrial recovery includes EPS facility scrap that is recycled but never served its intended purpose as a packaging material or other end-use application.</p>
  </section>

  <section class="total-band">
    <div class="total-block">
      <div class="total-year">2017 Total</div>
      <div class="total-unit">million pounds of EPS recycled</div>
      <div class="total-value">65.0</div>
    </div>
    <div class="total-photo" role="img" aria-label="Close-up photo of white expanded polystyrene with a molded recycling code"></div>
  </section>

  <h2 class="chart-title">EPS Recycling Post-Consumer &amp; Post-Industrial</h2>
  <p class="chart-subtitle">(millions of pounds)</p>

  <svg class="chart" viewBox="0 0 928 400" aria-label="Bar chart of EPS recycling by year">
    <g font-size="12" fill="#1f1a18">
      <line x1="148" y1="49" x2="157" y2="49" stroke="#1f1a18" stroke-width="1"/>
      <text x="165" y="53">POST-CONSUMER</text>
      <line x1="360" y1="49" x2="369" y2="49" stroke="#1f1a18" stroke-width="1"/>
      <text x="377" y="53">POST-INDUSTRIAL</text>
    </g>

    <g class="bars-consumer" fill="var(--green)">
      <rect x="74" y="238.1" width="49" height="127.9"/>
      <rect x="211" y="237.6" width="49" height="128.4"/>
      <rect x="345" y="193.4" width="49" height="172.6"/>
      <rect x="483" y="177.5" width="49" height="188.5"/>
      <rect x="620" y="42.4" width="49" height="323.6"/>
      <rect x="758" y="233" width="49" height="133"/>
    </g>
    <g class="bars-industrial" fill="var(--orange)">
      <rect x="129" y="285.9" width="49" height="80.1"/>
      <rect x="266" y="197" width="49" height="169"/>
      <rect x="401" y="182.1" width="49" height="183.9"/>
      <rect x="539" y="73.8" width="49" height="292.2"/>
      <rect x="676" y="79.9" width="49" height="286.1"/>
      <rect x="813" y="165.7" width="49" height="200.3"/>
    </g>

    <g font-size="14.5" text-anchor="middle" fill="var(--green-text)">
      <text x="98.5" y="232">24.9</text>
      <text x="235.5" y="231">25.0</text>
      <text x="369.5" y="187">33.6</text>
      <text x="507.5" y="171">36.7</text>
      <text x="644.5" y="36">63.0</text>
      <text x="782.5" y="227">25.9</text>
    </g>
    <g font-size="14.5" text-anchor="middle" fill="var(--orange)">
      <text x="153.5" y="280">15.6</text>
      <text x="290.5" y="191">32.9</text>
      <text x="425.5" y="176">35.8</text>
      <text x="563.5" y="68">56.9</text>
      <text x="700.5" y="74">55.7</text>
      <text x="837.5" y="160">39.0</text>
    </g>

    <line x1="65" y1="366.5" x2="862" y2="366.5" stroke="#b9b1ae" stroke-width="1"/>

    <g font-size="14" text-anchor="middle" fill="#1f1a18">
      <text x="126" y="382">2000</text>
      <text x="263" y="382">2004</text>
      <text x="398" y="382">2008</text>
      <text x="535" y="382">2012</text>
      <text x="672" y="382">2016</text>
      <text x="810" y="382">2017</text>
    </g>
  </svg>

  <p class="summary">Despite lower collection amounts reflected in 2017, EPS has historically enjoyed consistent growth since its inception in the early 1990’s. This decrease is a direct result of export restrictions on recycled plastics and a reprocessing plant closure that previously recycled large quantities of EPS. Newer EPS recycling technologies to facilitate EPS collection and reprocessing launched in 2018 indicate growth rates will continue on an upward trend in the future.</p>

  <div class="footer-blue"></div>
  <div class="footer-gold"></div>
</main>
</body>
</html>
```